Upscale business cards needed for family business

We need professional business cards created for several family members. We are a family business holding company. We would like these relatively simple and straightforward, but also with a unique element to set them apart. Probably stick with neutral and simple colors - white, grey etc. We need space for the traditional elements, including name, title, address, email/phone number. And we will be creating several from this template so it needs to be template that is easy to switch information in and out of.

Industry/Entity Type

Business

Contact Information for Business Card

Please include the attached Dunmore Ventures logo.

Requirements
Must have
• The attached Dunmore Ventures logo.

```html
<!DOCTYPE html>
<html lang="en">
<head>
<meta charset="utf-8">
<title>Dunmore Ventures – Business Card</title>
<link href="https://fonts.googleapis.com/css2?family=Cinzel:wght@400;700&family=Tinos:wght@400&display=swap" rel="stylesheet">
<style>
  :root {
    --page-bg: #1c1c1c;
    --card-black: #050505;
    --gold: #d9a521;
    --white: #f4f4f4;
    --divider: #8a8a8a;
  }
  * { margin: 0; padding: 0; box-sizing: border-box; }
  html, body {
    width: 1200px;
    height: 800px;
    overflow: hidden;
    background: var(--page-bg);
  }
  .stage {
    width: 1200px;
    height: 800px;
    display: flex;
    align-items: center;
    justify-content: center;
  }
  .business-card {
    position: relative;
    width: 1000px;
    height: 572px;
    background: var(--card-black);
    white-space: nowrap;
  }
  .card-frame {
    position: absolute;
    inset: 42px;
    border: 3px solid var(--gold);
  }
  .brand-name {
    position: absolute;
    top: 170px;
    left: 0;
    right: 0;
    text-align: center;
    font-family: "Cinzel", serif;
    font-weight: 400;
    font-size: 54px;
    letter-spacing: 2px;
    color: var(--white);
  }
  .person {
    position: absolute;
    top: 298px;
    left: 90px;
    width: 250px;
    text-align: right;
  }
  .person-name {
    font-family: "Cinzel", serif;
    font-weight: 700;
    font-size: 22px;
    line-height: 30px;
    color: var(--white);
    letter-spacing: 0.5px;
  }
  .person-title {
    font-family: "Tinos", serif;
    font-size: 17px;
    line-height: 24px;
    color: var(--gold);
  }
  .divider {
    position: absolute;
    top: 300px;
    width: 1.5px;
    height: 54px;
    background: var(--divider);
  }
  .divider--phones { left: 360px; }
  .divider--web { left: 575px; }
  .contact-list {
    position: absolute;
    top: 299px;
    list-style: none;
    font-family: "Tinos", serif;
    font-size: 20px;
    line-height: 28px;
    color: var(--white);
  }
  .contact-list--phones { left: 382px; }
  .contact-list--web { left: 597px; }
  .contact-list li {
    display: flex;
    align-items: center;
    gap: 10px;
  }
  .contact-list svg {
    width: 16px;
    height: 16px;
    flex: none;
  }
  .address {
    position: absolute;
    top: 378px;
    left: 245px;
    font-family: "Tinos", serif;
    font-size: 20px;
    line-height: 28px;
    color: var(--white);
  }
</style>
</head>
<body>
<main class="stage">
  <article class="business-card">
    <div class="card-frame"></div>

    <h1 class="brand-name">Dunmore Ventures</h1>

    <div class="person">
      <p class="person-name">EDWARD MARLOW</p>
      <p class="person-title">Managing director</p>
    </div>

    <span class="divider divider--phones"></span>

    <ul class="contact-list contact-list--phones">
      <li>
        <svg viewBox="0 0 16 16" aria-hidden="true"><path fill="var(--gold)" d="M3.6 1.2l2.3 2.6-1.3 1.8c.9 2 2.6 3.8 4.8 4.9l1.8-1.3 2.6 2.3-1.4 2.3C7.2 13.3 2.7 8.8 1.2 2.6z"/></svg>
        <span>0745-2219-6083</span>
      </li>
      <li>
        <svg viewBox="0 0 16 16" aria-hidden="true"><rect x="2" y="3" width="12" height="10" rx="2" fill="var(--gold)"/><rect x="4" y="5" width="8" height="3" fill="var(--card-black)"/><circle cx="8" cy="10.5" r="1" fill="var(--card-black)"/></svg>
        <span>0718-5402-3396</span>
      </li>
    </ul>

    <span class="divider divider--web"></span>

    <ul class="contact-list contact-list--web">
      <li>
        <svg viewBox="0 0 16 16" aria-hidden="true"><rect x="1.5" y="3.5" width="13" height="9" fill="var(--gold)"/><path d="M1.5 3.5l6.5 5 6.5-5" fill="none" stroke="var(--card-black)" stroke-width="1.2"/></svg>
        <span>emarlow@dunmoreventures.com</span>
      </li>
      <li>
        <svg viewBox="0 0 16 16" aria-hidden="true"><rect x="2" y="3" width="12" height="8" fill="none" stroke="var(--gold)" stroke-width="1.6"/><rect x="6" y="12" width="4" height="1.6" fill="var(--gold)"/></svg>
        <span>dunmoreventures.com</span>
      </li>
    </ul>

    <p class="address">48 Harbour Lane, Suite 210, Westbrook, State, Zip Code</p>
  </article>
</main>
</body>
</html>
```